A-Stand Directional Sign Design

Objective:
We need a professional graphic design for an A-Stand sign that will guide customers arriving in our parking lot to our office. The design should be visually clear, welcoming, and aligned with our brand identity.
REQUIREMENTS:
Two versions of the design:
- One with an arrow pointing left
- One with an arrow pointing right
(This allows us to place the A-Stand anywhere and flip the graphic as needed.)
DIMENSIONS:
- Viewable Area: 30" x 40"
BRAND ALIGNMENT:
- Colors, fonts, and overall style should match our website: www.glidecrest.com
- Clean, modern, and professional look consistent with our aviation/tourism brand
CONTENT:
- Clear directional arrow (left or right depending on version)
- Text: “Office Entrance” or similar concise wording (designers may propose alternatives if they improve clarity)
READABILITY:
- Bold, high-contrast design for visibility from a distance
- Simple layout that avoids clutter
DELIVERABLES:
- Final artwork in print-ready format (PDF preferred)
- Two versions: Arrow Left and Arrow Right
DESIGN GOAL:
Ensure customers can easily find our office upon arrival, while reinforcing glideCREST’s professional and welcoming brand image.
Target Market(s)
Tourism
Look and feel

```html
<!DOCTYPE html>
<html lang="en">
<head>
<meta charset="utf-8">
<title>glideCREST – A-Stand Directional Signs</title>
<link href="https://fonts.googleapis.com/css2?family=Montserrat:wght@700;800&display=swap" rel="stylesheet">
<style>
  :root {
    --page-bg: #ffffff;
    --sign-white: #ffffff;
    --brand-deep: #0049b7;
    --brand-bright: #0a66f0;
    --brand-name: #0a6fd6;
    --ink-light: #ffffff;
    --chevron-strong: #ececec;
    --chevron-mid: #bccbe2;
    --chevron-soft: #5f89cb;
  }
  * { margin: 0; padding: 0; box-sizing: border-box; }
  html, body {
    width: 1200px;
    height: 811px;
    overflow: hidden;
    background: var(--page-bg);
    font-family: "Montserrat", Arial, sans-serif;
  }
  .sign-set {
    position: relative;
    width: 1200px;
    height: 811px;
  }
  .sign {
    position: absolute;
    top: 60px;
    width: 519px;
    height: 692px;
    background: var(--sign-white);
    box-shadow: 0 14px 40px rgba(0, 0, 0, 0.32);
    overflow: hidden;
  }
  .sign--left { left: 53px; }
  .sign--right { left: 612px; }
  .sign__art {
    position: absolute;
    inset: 0;
    width: 100%;
    height: 100%;
  }
  .brand {
    position: absolute;
    top: 78px;
    left: 0;
    width: 100%;
    display: flex;
    justify-content: center;
    align-items: center;
    gap: 10px;
  }
  .brand__dot {
    width: 22px;
    height: 22px;
    border-radius: 50%;
    background: var(--brand-name);
  }
  .brand__name {
    font-size: 40px;
    font-weight: 800;
    color: var(--brand-name);
    letter-spacing: 0.5px;
    line-height: 1;
  }
  .headline {
    position: absolute;
    top: 254px;
    left: 0;
    width: 100%;
    text-align: center;
    color: var(--ink-light);
    font-weight: 800;
    font-size: 59px;
    line-height: 60px;
    letter-spacing: 1px;
    text-transform: uppercase;
  }
  .divider {
    position: absolute;
    top: 405px;
    left: 162px;
    width: 195px;
    height: 2px;
    background: var(--ink-light);
  }
  .web-address {
    position: absolute;
    top: 605px;
    left: 0;
    width: 100%;
    text-align: center;
    color: var(--ink-light);
    font-weight: 700;
    font-size: 14px;
    letter-spacing: 0.6px;
    text-transform: uppercase;
  }
</style>
</head>
<body>
<main class="sign-set">

  <section class="sign sign--left" aria-label="Office entrance sign, arrow pointing left">
    <svg class="sign__art" viewBox="0 0 1004 1339" preserveAspectRatio="none" aria-hidden="true">
      <path d="M0 554 C260 360 640 270 1004 409 L1004 1339 L0 1339 Z" fill="var(--brand-bright)"/>
      <path d="M0 580 C270 390 650 300 1004 413 L1004 1339 L0 1339 Z" fill="var(--brand-deep)"/>
      <g fill="none" stroke-width="60" stroke-linecap="round" stroke-linejoin="round">
        <polyline points="734,882 644,983 734,1084" stroke="var(--chevron-soft)"/>
        <polyline points="548,882 458,983 548,1084" stroke="var(--chevron-mid)"/>
        <polyline points="362,882 272,983 362,1084" stroke="var(--chevron-strong)"/>
      </g>
    </svg>
    <div class="brand"><span class="brand__dot"></span><span class="brand__name">glideCREST</span></div>
    <h1 class="headline">Office<br>Entrance</h1>
    <div class="divider"></div>
    <p class="web-address">www.glidecrest.com</p>
  </section>

  <section class="sign sign--right" aria-label="Office entrance sign, arrow pointing right">
    <svg class="sign__art" viewBox="0 0 1004 1339" preserveAspectRatio="none" aria-hidden="true">
      <path d="M0 554 C260 360 640 270 1004 409 L1004 1339 L0 1339 Z" fill="var(--brand-bright)"/>
      <path d="M0 580 C270 390 650 300 1004 413 L1004 1339 L0 1339 Z" fill="var(--brand-deep)"/>
      <g fill="none" stroke-width="60" stroke-linecap="round" stroke-linejoin="round">
        <polyline points="270,882 360,983 270,1084" stroke="var(--chevron-soft)"/>
        <polyline points="456,882 546,983 456,1084" stroke="var(--chevron-mid)"/>
        <polyline points="642,882 732,983 642,1084" stroke="var(--chevron-strong)"/>
      </g>
    </svg>
    <div class="brand"><span class="brand__dot"></span><span class="brand__name">glideCREST</span></div>
    <h1 class="headline">Office<br>Entrance</h1>
    <div class="divider"></div>
    <p class="web-address">www.glidecrest.com</p>
  </section>

</main>
</body>
</html>
```